"Temo" - Movie Poster for Japanese Black and White Feature Film

We are re-editing and grading an obscure Japanese language film. The film was shot on 35mm quite a few years ago. We have a number of colour stills from the movie. The movies title TEMO is currently being hand drawn by a Japanese artist and will be available shortly. It is mystery drama that cuts between modern and not so modern Japan.
It is not a Japanese horror film, but is plays a little bit spooky in parts. The main character is a writer. He is suffering from writers block. He drinks heavily and fades in and out of his own story to the point where the lines are quite blurred.
Title in Japanese - Guide Text has been uploaded.
狂
華
We are looking for a designer to produce the key art / movie poster. At this stage we are open to all design ideas, although we would like the title to run large down the poster somewhere. The poster will be used on the movies website, along with RELZ and QPO. Although there will not be a theatrical release, we will be doing a limited addition run of the actual poster. We have attached a number of low quality stills to get this project started. Additional format variations based on the original poster design may also be required.
Once this project has been completed we will require additional work for another title releases. So would be ideally looking for a designer who is interested in creating a distinctive key art style over a slow series of releases.
Any questions, please let me know.
Thank you. Namika.
Reason: Working through remaining design submissions.
Thank you.
Reason: We just need a little more time to finalise the text / typography.
Thank you for your patience.
Reason: Finishing up now.

```html
<!DOCTYPE html>
<html lang="en">
<head>
<meta charset="utf-8">
<title>狂華 – Poster</title>
<link rel="stylesheet" href="https://fonts.googleapis.com/css2?family=Oswald:wght@300;400;700&family=Noto+Serif+JP:wght@700&display=swap">
<style>
  :root {
    --ink: #070605;
    --amber: #e88a1c;
    --paper: #f2ede4;
    --scene-dark: #0b0a07;
    --scene-warm: #3a2a14;
  }
  html, body {
    margin: 0;
    padding: 0;
    width: 805px;
    height: 1200px;
    overflow: hidden;
    background: var(--ink);
  }
  .poster {
    position: relative;
    width: 805px;
    height: 1200px;
    background: var(--ink);
    overflow: hidden;
    font-family: "Oswald", sans-serif;
  }
  .night-scene {
    position: absolute;
    left: 0;
    top: 720px;
    width: 805px;
    height: 480px;
    background:
      radial-gradient(ellipse 130px 60px at 185px 215px, rgba(150, 100, 45, 0.55), transparent 75%),
      radial-gradient(ellipse 220px 40px at 480px 215px, rgba(90, 70, 35, 0.35), transparent 80%),
      linear-gradient(to bottom, var(--ink) 0%, var(--scene-dark) 30%, #1c160c 45%, #15120b 60%, var(--scene-dark) 100%);
  }
  .studio-line {
    position: absolute;
    top: 46px;
    left: 0;
    width: 100%;
    margin: 0;
    text-align: center;
    color: var(--amber);
    font-size: 17px;
    font-weight: 400;
    line-height: 20px;
    letter-spacing: 0.62em;
    text-indent: 0.62em;
  }
  .tagline {
    position: absolute;
    top: 78px;
    left: 0;
    width: 100%;
    margin: 0;
    text-align: center;
    color: var(--paper);
    font-size: 11.5px;
    font-weight: 400;
    line-height: 1.45;
    letter-spacing: 0.21em;
  }
  .title {
    position: absolute;
    top: 290px;
    left: 0;
    width: 100%;
    margin: 0;
    text-align: center;
    color: var(--amber);
    font-family: "Noto Serif JP", serif;
    font-weight: 700;
    font-size: 150px;
    line-height: 170px;
  }
  .title span { display: block; }
  .credits {
    position: absolute;
    top: 994px;
    left: 12px;
    width: 100%;
    text-align: center;
  }
  .credit-role {
    margin: 0;
    color: var(--paper);
    font-size: 9.5px;
    font-weight: 700;
    letter-spacing: 0.04em;
  }
  .credit-name {
    margin: 0 0 10px;
    color: var(--amber);
    font-size: 17px;
    font-weight: 400;
    letter-spacing: 0.14em;
    line-height: 1.25;
  }
</style>
</head>
<body>
  <main class="poster">
    <div class="night-scene" role="img" aria-label="Night photograph of a dimly lit station building beside empty rail tracks and low barriers"></div>

    <p class="studio-line">A ORVALE PRODUCTION</p>
    <p class="tagline">BRIGHT, SHARP IMAGES WEAVE A FRAGMENTED DAYDREAM OF FEAR, VIOLENCE AND LOVE LOST,<br>TOLD FROM SEVERAL POINTS OF VIEW.</p>

    <h1 class="title" lang="ja"><span>狂</span><span>華</span></h1>

    <section class="credits">
      <p class="credit-role">WRITER · PRODUCER</p>
      <p class="credit-name">NAMIKA SORANO</p>
      <p class="credit-role">DIRECTOR</p>
      <p class="credit-name">DALE ORWIN</p>
    </section>
  </main>
</body>
</html>
```